Webdesign für eine Hausbau Firma
Zielgruppe
Das Design soll Bauherren gefallen. Wir bauen Massiv Häuser.
Aufgabenstellung
Unser Logo muss gut eingebunden sein. Helles Design mit unseren Logo Farben. Einen Bereich für Kunden mit Login. Dieser sollte aufgebaut sein als blog wo Kunden Bilder und Kommentare posten können.

```html
<!DOCTYPE html>
<html lang="de">
<head>
<meta charset="utf-8">
<title>Nordwerk Steinbau – Massivhäuser</title>
<link href="https://fonts.googleapis.com/css2?family=Montserrat:wght@400;500;600;700&display=swap" rel="stylesheet">
<style>
:root{
  --teal:#19a39b;
  --teal-dark:#12867f;
  --text:#4a4a4a;
  --muted:#8a8a8a;
  --field:#eeeeee;
  --card:#f0f0f0;
  --footer:#3f3f41;
  --stage:#e9e9e9;
  --white:#ffffff;
}
*{box-sizing:border-box;margin:0;padding:0}
html,body{width:1200px;height:4764px;overflow:hidden}
body{background:var(--stage);font-family:"Montserrat",sans-serif;color:var(--text)}
.page{position:absolute;left:40px;top:66px;width:1120px;height:4582px;background:var(--white);box-shadow:0 4px 18px rgba(0,0,0,.25);overflow:hidden}
.abs{position:absolute}

/* hero */
.hero-photo{position:absolute;left:0;top:0;width:1120px;height:580px;
  background:linear-gradient(180deg,#bcd3e8 0%,#d9e6f1 35%,#eef0ee 52%,#c9cdc8 62%,#7fa14f 75%,#5f8a38 100%);
  clip-path:polygon(0 0,100% 0,100% 395px,50% 580px,0 395px)}
.brand{position:absolute;left:0;width:1120px;top:72px;text-align:center;font-size:22px;font-weight:600;letter-spacing:1.5px;color:var(--teal-dark)}
.nav{position:absolute;left:144px;top:202px;height:28px;display:flex;background:var(--white);border-bottom:3px solid var(--teal)}
.nav a{display:block;padding:0 12px;font-size:15px;font-weight:500;line-height:28px;color:#333;text-decoration:none;border-right:3px solid var(--stage)}
.nav a:last-child{border-right:none}

/* shared */
.section-title{position:absolute;left:0;width:1120px;text-align:center;font-size:27px;font-weight:400;letter-spacing:1px;color:var(--teal)}
.divider{position:absolute;left:144px;width:830px;height:3px;background:linear-gradient(90deg,var(--teal),#9fd6d2 70%,#e6f3f2)}
.body-text{font-size:12.5px;line-height:17px;color:var(--text);text-align:center}
.btn{display:inline-block;background:var(--teal);color:var(--white);font-size:12.5px;font-weight:500;padding:0 10px;line-height:26px;letter-spacing:.3px}

/* features */
.feature{position:absolute;top:690px;width:280px;text-align:center}
.feature svg{display:block;margin:0 auto 12px}
.feature h3{font-size:18px;font-weight:400;color:var(--teal);margin-bottom:8px;letter-spacing:.5px}

/* show houses */
.house{position:absolute;top:1115px;width:235px;text-align:center}
.house-photo{width:235px;height:258px;clip-path:polygon(0 0,100% 0,100% 200px,50% 258px,0 200px)}
.house h3{font-size:18px;font-weight:400;color:var(--teal);margin:26px 0 4px;letter-spacing:.5px}
.house .btn{margin-top:18px}

/* sites */
.site{position:absolute;top:1791px;width:438px;height:234px}
.site-photo{width:100%;height:100%;background:linear-gradient(160deg,#7fa8d4 0%,#b7cce2 40%,#d7d4cc 65%,#9a958d 100%)}
.site-label{position:absolute;left:0;bottom:0;width:238px;height:56px;background:var(--teal);color:var(--white);padding:10px 14px}
.site-label strong{display:block;font-size:14px;font-weight:600}
.site-label span{font-size:11.5px}

/* testimonials */
.quote{position:absolute;top:2295px;height:219px;background:var(--card);padding:24px 18px 0 64px}
.quote-mark{position:absolute;left:0;top:22px;width:50px;height:34px;background:var(--teal);color:var(--white);font-size:40px;font-weight:700;line-height:46px;text-align:center;font-style:italic}
.quote p{font-size:12.5px;line-height:19.5px;color:var(--text)}
.quote cite{display:block;margin-top:8px;font-size:10.5px;font-weight:600;font-style:normal;color:var(--teal)}

/* partners */
.partner-text{position:absolute;top:2765px;width:440px;font-size:11.5px;line-height:21px;text-align:justify}
.partners{position:absolute;left:260px;top:2884px;width:600px;display:flex;justify-content:space-between}
.partner-badge{width:54px;height:44px;background:#a9a9a9;border-radius:6px}

/* client area */
.tile{position:absolute}
.login{position:absolute;left:107px;top:3153px;width:386px;height:213px;background:linear-gradient(135deg,#1fb0a6,#148e86);padding:28px 36px;color:var(--white)}
.login h3{font-size:19px;font-weight:500;margin-bottom:8px}
.login .field{width:270px;height:32px;background:var(--white);color:#777;font-size:12px;line-height:32px;padding:0 8px;margin-bottom:16px}
.login a{position:absolute;right:80px;bottom:36px;color:var(--white);font-size:12px;text-decoration:underline}

/* contact */
.form-field{position:absolute;background:var(--field);font-size:12px;color:#666;padding:14px 12px}

/* footer */
.footer-col{position:absolute;top:4191px}
.footer-col h4{font-size:12px;font-weight:500;color:var(--teal);margin-bottom:9px}
.footer-col li{list-style:none;font-size:9.5px;line-height:18.5px;color:#666}
.newsletter{width:210px;height:26px;border:1.5px solid var(--teal);font-size:9.5px;line-height:23px;padding:0 8px;color:#666;position:relative}
.footer-bar{position:absolute;left:0;top:4342px;width:1120px;height:240px;background:var(--footer);color:#ddd}
.footer-brand{position:absolute;left:107px;top:50px;display:flex;align-items:center;gap:10px}
.footer-brand span{font-size:16px;font-weight:600;letter-spacing:1px;color:var(--white)}
.footer-brand i{display:block;width:22px;height:22px;border:2px solid var(--white)}
.footer-about{position:absolute;left:314px;top:48px;width:360px;font-size:9.5px;line-height:17px}
.social{position:absolute;left:797px;top:70px;display:flex;gap:18px}
.social i{display:block;width:40px;height:40px;background:var(--white)}
.footer-rule{position:absolute;left:107px;top:156px;width:900px;height:1px;background:#6a6a6c}
.copyright{position:absolute;left:107px;top:166px;font-size:9.5px}
.legal{position:absolute;right:113px;top:166px;font-size:9.5px;display:flex;gap:12px;text-decoration:underline}
</style>
</head>
<body>
<div class="page">

  <!-- hero -->
  <div class="hero-photo" role="img" aria-label="Fotografie eines modernen weißen Flachdach-Bungalows mit Rasenfläche und Birken unter blauem Himmel"></div>
  <div class="brand">NORDWERK STEINBAU</div>
  <nav class="nav">
    <a>START</a><a>MUSTERHÄUSER</a><a>AKTUELLES</a><a>UNSERE PARTNER</a><a>KUNDENBEREICH</a><a>KONTAKT</a>
  </nav>

  <!-- process -->
  <div class="feature" style="left:105px">
    <svg width="72" height="72" viewBox="0 0 72 72" fill="none" stroke="var(--teal)" stroke-width="2.5"><rect x="4" y="4" width="64" height="64"/><rect x="12" y="12" width="48" height="48"/><path d="M12 34h20v26M32 22h28M44 22v16h16"/></svg>
    <h3>PLANUNG</h3>
    <p class="body-text">Nullam dictum felis eu pede mollis pretium. Integer tincidunt. Cras dapibus. Vivamus elementum semper nisi. Aenean vulputate eleifend tellus.</p>
  </div>
  <div class="feature" style="left:419px">
    <svg width="90" height="72" viewBox="0 0 90 72" fill="none" stroke="var(--teal)" stroke-width="2.5"><path d="M14 54a31 31 0 0 1 62 0"/><path d="M6 54h78v8H6z"/><path d="M36 22v28M54 22v28M36 22h18"/></svg>
    <h3>BAUPHASE</h3>
    <p class="body-text">Nullam dictum felis eu pede mollis pretium. Integer tincidunt. Cras dapibus. Vivamus elementum semper nisi. Aenean vulputate eleifend tellus.</p>
  </div>
  <div class="feature" style="left:748px">
    <svg width="86" height="72" viewBox="0 0 86 72" fill="none" stroke="var(--teal)" stroke-width="2.5"><path d="M4 28L43 6l39 22"/><path d="M12 24v44h62V24"/><rect x="22" y="36" width="18" height="14"/><path d="M31 36v14"/><rect x="48" y="36" width="16" height="32"/></svg>
    <h3>ÜBERGABE</h3>
    <p class="body-text">Nullam dictum felis eu pede mollis pretium. Integer tincidunt. Cras dapibus. Vivamus elementum semper nisi. Aenean vulputate eleifend tellus.</p>
  </div>

  <div class="divider" style="top:958px"></div>

  <!-- show houses -->
  <h2 class="section-title" style="top:1056px">MUSTERHÄUSER</h2>
  <div class="house" style="left:107px">
    <div class="house-photo" role="img" aria-label="Foto einer weißen Stadtvilla mit großen Fenstern" style="background:linear-gradient(180deg,#f1f1ef,#cfd0cb 60%,#6d8f4e)"></div>
    <h3>LOREM IPSUM</h3>
    <p class="body-text">Nullam dictum felis eu pede mollis pretium. Integer tincidunt. Cras dapibus. Vivamus elementum semper nisi. Aenean vulputate eleifend tellus.</p>
    <span class="btn">MEHR ERFAHREN</span>
  </div>
  <div class="house" style="left:439px">
    <div class="house-photo" role="img" aria-label="Foto eines modernen Hauses mit dunkler Fassade und Holzelementen" style="background:linear-gradient(180deg,#5e8fd0,#8ea9c8 35%,#4d4d55 60%,#9c8e80)"></div>
    <h3>LOREM IPSUM</h3>
    <p class="body-text">Nullam dictum felis eu pede mollis pretium. Integer tincidunt. Cras dapibus. Vivamus elementum semper nisi. Aenean vulputate eleifend tellus.</p>
    <span class="btn">MEHR ERFAHREN</span>
  </div>
  <div class="house" style="left:772px">
    <div class="house-photo" role="img" aria-label="Foto eines Einfamilienhauses mit Satteldach und Garage" style="background:linear-gradient(180deg,#9db7d9,#cdd6df 35%,#6f6f70 60%,#b7b2a8)"></div>
    <h3>LOREM IPSUM</h3>
    <p class="body-text">Nullam dictum felis eu pede mollis pretium. Integer tincidunt. Cras dapibus. Vivamus elementum semper nisi. Aenean vulputate eleifend tellus.</p>
    <span class="btn">MEHR ERFAHREN</span>
  </div>

  <div class="divider" style="top:1630px"></div>

  <!-- current sites -->
  <h2 class="section-title" style="top:1706px">AKTUELLE BAUSTELLEN</h2>
  <div class="site" style="left:107px">
    <div class="site-photo" role="img" aria-label="Foto eines Rohbaus mit Dachstuhl vor blauem Himmel"></div>
    <div class="site-label"><strong>LOREM IPSUM ET DOLOR</strong><span>Jetzt entdecken &gt;</span></div>
  </div>
  <div class="site" style="left:569px">
    <div class="site-photo" role="img" aria-label="Foto eines Rohbaus mit Dachstuhl vor blauem Himmel"></div>
    <div class="site-label"><strong>LOREM IPSUM ET DOLOR</strong><span>Jetzt entdecken &gt;</span></div>
  </div>

  <div class="divider" style="top:2132px"></div>

  <!-- testimonials -->
  <h2 class="section-title" style="top:2220px">DAS SAGEN UNSERE KUNDEN</h2>
  <div class="quote" style="left:107px;width:286px"><div class="quote-mark">”</div><p>Maecenas nec odio et ante tincidunt tempus. Donec vitae sapien ut libero venenatis faucibus. Nullam quis ante. Etiam sit amet orci eget eros faucibus tincidunt. Duis leo. Sed fringilla mauris sit amet nibh. Donec sodales sagittis magna.</p><cite>Kunde xy</cite></div>
  <div class="quote" style="left:408px;width:299px"><div class="quote-mark">”</div><p>Maecenas nec odio et ante tincidunt tempus. Donec vitae sapien ut libero venenatis faucibus. Nullam quis ante. Etiam sit amet orci eget eros faucibus tincidunt. Duis leo. Sed fringilla mauris sit amet nibh. Donec sodales sagittis magna.</p><cite>Kunde xy</cite></div>
  <div class="quote" style="left:724px;width:282px"><div class="quote-mark">”</div><p>Maecenas nec odio et ante tincidunt tempus. Donec vitae sapien ut libero venenatis faucibus. Nullam quis ante. Etiam sit amet orci eget eros faucibus tincidunt. Duis leo. Sed fringilla mauris sit amet nibh. Donec sodales sagittis magna.</p><cite>Kunde xy</cite></div>
  <span class="btn abs" style="left:492px;top:2546px">MEHR LESEN</span>

  <div class="divider" style="top:2643px"></div>

  <!-- partners -->
  <h2 class="section-title" style="top:2718px">UNSERE PARTNER</h2>
  <p class="partner-text" style="left:107px">Lorem ipsum dolor sit amet, consectetuer adipiscing elit. Aenean commodo ligula eget dolor. Aenean massa. Cum sociis natoque penatibus et magnis dis parturient montes, nascetur ridiculus mus.</p>
  <p class="partner-text" style="left:566px;text-align:left">Donec quam felis, ultricies nec, pellentesque eu, pretium quis, sem. Nulla consequat massa quis enim. Donec pede justo, fringilla vel, aliquet nec, vulputate eget, arcu. In enim justo, rhoncus ut, imperdiet a.</p>
  <div class="partners">
    <div class="partner-badge" aria-label="Partner 1"></div>
    <div class="partner-badge" aria-label="Partner 2"></div>
    <div class="partner-badge" aria-label="Partner 3"></div>
    <div class="partner-badge" aria-label="Partner 4"></div>
    <div class="partner-badge" aria-label="Partner 5"></div>
    <div class="partner-badge" aria-label="Partner 6"></div>
  </div>

  <div class="divider" style="top:3022px"></div>

  <!-- client area -->
  <h2 class="section-title" style="top:3092px">UNSER KUNDENBEREICH</h2>
  <div class="tile" style="left:0;top:3153px;width:107px;height:213px;background:linear-gradient(180deg,#a9c3e0,#c8c6c0 60%,#6f8c4a)" role="img" aria-label="Kundenfoto: Haus mit Satteldach"></div>
  <div class="tile" style="left:493px;top:3153px;width:436px;height:213px;background:linear-gradient(180deg,#4f86cf,#8aa6c8 40%,#4b4b52 65%,#9b8c7b)" role="img" aria-label="Kundenfoto: modernes Haus mit dunkler Fassade"></div>
  <div class="tile" style="left:929px;top:3153px;width:191px;height:213px;background:linear-gradient(180deg,#f2f2f0,#cfd1cc 60%,#6b8d4c)" role="img" aria-label="Kundenfoto: weiße Stadtvilla"></div>
  <div class="tile" style="left:0;top:3366px;width:196px;height:213px;background:linear-gradient(160deg,#7fa8d4,#c9d3dc 50%,#9a958d)" role="img" aria-label="Kundenfoto: Rohbau mit Dachstuhl"></div>
  <div class="tile" style="left:196px;top:3366px;width:347px;height:213px;background:linear-gradient(180deg,#a7bedc,#d3d6d8 35%,#6b6b6c 62%,#b3aea5)" role="img" aria-label="Kundenfoto: Einfamilienhaus mit Garage"></div>
  <div class="tile" style="left:543px;top:3366px;width:256px;height:213px;background:linear-gradient(180deg,#bcd3e8,#e6e8e6 50%,#7c9f4f)" role="img" aria-label="Kundenfoto: Bungalow mit Garten"></div>
  <div class="tile" style="left:799px;top:3366px;width:321px;height:213px;background:linear-gradient(135deg,#f3f1ee,#dcd8d2 55%,#a9a39b)" role="img" aria-label="Kundenfoto: heller Wohnraum mit Kaminofen"></div>
  <div class="login">
    <h3>LOGIN</h3>
    <div class="field">Benutzername</div>
    <div class="field">Kennwort</div>
    <a>anmelden</a>
  </div>

  <div class="divider" style="top:3692px"></div>

  <!-- contact -->
  <h2 class="section-title" style="top:3764px">KONTAKT AUFNEHMEN</h2>
  <div class="form-field" style="left:251px;top:3827px;width:299px;height:44px">Ihr Name</div>
  <div class="form-field" style="left:251px;top:3884px;width:299px;height:44px">Ihre E-Mail-Adresse</div>
  <div class="abs" style="left:393px;top:3941px;width:157px;height:47px;background:var(--teal);color:var(--white);font-size:13px;text-align:center;line-height:47px">absenden</div>
  <div class="form-field" style="left:567px;top:3827px;width:297px;height:161px">Ihre Nachricht</div>

  <!-- footer links -->
  <div class="footer-col" style="left:107px"><h4>NAVIGATION</h4><ul><li>Start</li><li>Musterhäuser</li><li>Aktuelle Baustellen</li><li>Unsere Partner</li><li>Unser Kundenbereich</li></ul></div>
  <div class="footer-col" style="left:336px"><h4>INFORMATION</h4><ul><li>Beispiel-Link 1</li><li>Beispiel-Link 2</li><li>Beispiel-Link 3</li><li>Beispiel-Link 4</li><li>Beispiel-Link 5</li></ul></div>
  <div class="footer-col" style="left:554px"><h4>UNTERNEHMEN</h4><ul><li>Beispiel-Link 1</li><li>Beispiel-Link 2</li><li>Beispiel-Link 3</li></ul></div>
  <div class="footer-col" style="left:794px"><h4>NEWSLETTER ABONNIEREN</h4>
    <div class="newsletter">Ihre E-Mail-Adresse
      <svg class="abs" style="right:5px;top:6px" width="8" height="12" viewBox="0 0 8 12" fill="none" stroke="var(--teal)" stroke-width="1.5"><path d="M1 1l5 5-5 5"/></svg>
    </div>
  </div>

  <footer class="footer-bar">
    <div class="footer-brand"><i></i><span>NORDWERK STEINBAU</span></div>
    <p class="footer-about">Vivamus elementum semper nisi. Aenean vulputate eleifend tellus. Aenean leo ligula consequat vitae, eleifend ac, enim. Aliquam lorem ante, viverra quis tellus. Phasellus viverra nulla ut metus varius laoreet. Maecenas tempus, tellus eget con dimentum rhoncus, sem quam semper libero, sit amet.</p>
    <div class="social"><i aria-label="Soziales Netzwerk 1"></i><i aria-label="Soziales Netzwerk 2"></i><i aria-label="Soziales Netzwerk 3"></i><i aria-label="Soziales Netzwerk 4"></i></div>
    <div class="footer-rule"></div>
    <div class="copyright">Copyright © 2017 Nordwerk Steinbau</div>
    <div class="legal"><span>AGB</span><span>Impressum</span><span>Datenschutz</span></div>
  </footer>
</div>
</body>
</html>
```